Kovrilex - presentation for a remote DBA team offering data platform management

We need a website design for wordpress site called Kovrilex.cz
We deliver remote database and data platform administration and development, oversee the database administrators, consult and train the personnel responsible for the database operations. The website should include several sections, home page with graphics elements supporting the name and service - remote dba work; blog section; service introduction and description, team introduction and description, download section for documents, presentations etc.

Target Market(s)

small and medium business companies requiring remote DBA service

Number of Pages Required

3 page

Font styles to use
Sans Serif

Colors

Designer to choose colors to be used in the design.

Requirements
Must have
• The website should have several sections to introduce the services, blog, team introduction, downloads

```html
<!DOCTYPE html>
<html lang="en">
<head>
<meta charset="utf-8">
<title>Kovrilex – Remote Database Administration</title>
<link href="https://fonts.googleapis.com/css2?family=Montserrat:wght@400;500;600;700;800&family=Open+Sans:wght@400;600&display=swap" rel="stylesheet">
<style>
:root{
  --blue:#1d9bf0;
  --blue-dark:#0f86db;
  --purple-1:#2c1580;
  --purple-2:#5a27c4;
  --purple-3:#8a3bd8;
  --ink:#1f2330;
  --muted:#8a8f9c;
  --line:#e3e6ec;
  --white:#ffffff;
  --footer:#f3f1ef;
}
*{box-sizing:border-box;margin:0;padding:0}
html,body{width:1200px;height:3620px;overflow:hidden;background:var(--white)}
body{font-family:"Open Sans",Arial,sans-serif;color:var(--ink);position:relative}
h1,h2,h3,h4,.brand,.nav,.btn{font-family:"Montserrat",Arial,sans-serif}
section,header,footer{position:absolute;left:0;width:1200px}
.circle-btn{position:absolute;width:44px;height:44px;border-radius:50%;display:flex;align-items:center;justify-content:center}
.circle-btn.outline{border:2px solid var(--blue);background:var(--white)}
.circle-btn.solid{background:var(--blue)}
.photo{position:absolute}

/* HERO */
.hero{top:0;height:600px;background:linear-gradient(120deg,var(--purple-1) 0%,var(--purple-2) 55%,var(--purple-3) 100%);color:var(--white)}
.brand{position:absolute;left:40px;top:30px;display:flex;align-items:center;gap:10px;font-weight:700;font-size:22px;letter-spacing:2px}
.brand .mark{width:34px;height:34px;border-radius:50%;border:2px solid var(--white)}
.nav{position:absolute;left:392px;top:38px;display:flex;gap:34px;font-size:14px;font-weight:600;letter-spacing:.5px}
.nav .active{position:relative}
.nav .active::after{content:"";position:absolute;left:0;right:0;bottom:-8px;height:2px;background:var(--blue)}
.nav .phone{color:#7fd0ff}
.btn-download{position:absolute;left:1020px;top:28px;height:40px;padding:0 20px;border-radius:20px;background:var(--white);color:var(--ink);font-size:13px;font-weight:700;display:flex;align-items:center;gap:8px}
.hero h1{position:absolute;left:136px;top:246px;width:640px;font-size:30px;line-height:1.35;font-weight:700}
.btn-consult{position:absolute;left:136px;top:392px;height:38px;padding:0 26px;border:2px solid var(--white);border-radius:20px;font-size:13px;font-weight:700;display:flex;align-items:center}
.hero-art{position:absolute;left:650px;top:90px;width:500px;height:470px;border-radius:20px;background:radial-gradient(circle at 55% 50%,rgba(76,200,255,.55),rgba(120,60,220,.25) 60%,transparent 75%)}

/* WELCOME */
.welcome{top:640px;height:240px}
.welcome h2{position:absolute;left:224px;top:70px;font-size:22px;font-weight:700}
.welcome h2 sup{font-size:11px}
.welcome .sub{position:absolute;left:224px;top:106px;font-size:13px;color:var(--muted)}
.welcome p{position:absolute;left:640px;top:64px;width:300px;font-size:12px;line-height:1.75;color:var(--muted)}

/* FEATURES */
.features{top:940px;height:720px;background:var(--blue);color:var(--white)}
.features h3{font-size:22px;font-weight:700;line-height:1.35}
.features p{font-size:12px;line-height:1.75;color:rgba(255,255,255,.85)}
.feature-a{position:absolute;left:640px;top:96px;width:360px}
.feature-b{position:absolute;left:130px;top:404px;width:430px}
.feature p{margin-top:14px}
.learn{display:flex;align-items:center;gap:12px;margin-top:18px;font-family:"Montserrat",Arial,sans-serif;font-size:11px;font-weight:700;letter-spacing:1px}
.learn .dot{width:28px;height:28px;border-radius:50%;background:var(--white);display:flex;align-items:center;justify-content:center}

/* SERVICES */
.services{top:1720px;height:330px}
.service{position:absolute;top:0;width:250px;text-align:center}
.service .icon{width:70px;height:70px;margin:0 auto}
.service h4{margin-top:22px;font-size:15px;font-weight:700;color:var(--blue)}
.service p{margin-top:12px;font-size:12px;line-height:1.7;color:var(--muted)}
.service .circle-btn{left:103px;top:236px}

/* TEAM */
.team{top:2064px;height:420px;background:var(--blue)}
.member{position:absolute;top:68px;width:224px;height:290px}
.member .portrait{position:absolute;inset:0;background:linear-gradient(180deg,#c9ced8,#7d8696)}
.member.featured{top:64px;height:298px;box-shadow:0 14px 30px rgba(0,0,0,.25)}
.member .name{position:absolute;left:0;right:0;bottom:22px;text-align:center;color:var(--white);font-family:"Montserrat",Arial,sans-serif;font-size:19px;font-weight:700}
.member .role{position:absolute;left:0;right:0;bottom:6px;text-align:center;color:var(--white);font-size:10px}
.team .arrow{position:absolute;top:198px}

/* BLOG */
.blog{top:2540px;height:520px}
.blog-card{position:absolute;left:192px;top:16px;width:400px;height:400px;overflow:hidden}
.blog-card .visual{position:absolute;inset:0;background:linear-gradient(150deg,#d7dbe2 0%,#8ea5c6 45%,#2e4f8c 100%)}
.blog-card .shade{position:absolute;inset:0;background:linear-gradient(180deg,transparent 45%,rgba(10,20,40,.75))}
.tag{position:absolute;left:0;top:0;background:var(--blue);color:var(--white);font-family:"Montserrat",Arial,sans-serif;font-size:10px;font-weight:700;letter-spacing:1px;padding:7px 16px}
.blog-card .date{position:absolute;left:30px;top:238px;color:var(--white);font-size:10px;letter-spacing:1px}
.blog-card h3{position:absolute;left:30px;top:262px;width:300px;color:var(--white);font-size:22px;line-height:1.3;font-weight:700}
.blog-list{position:absolute;left:640px;top:20px;width:440px}
.post{padding:18px 0 22px;border-bottom:1px solid var(--line)}
.post:first-child{padding-top:0}
.post:last-child{border-bottom:0}
.post .date{font-size:10px;color:var(--muted);letter-spacing:1px}
.post h4{margin-top:8px;font-size:15px;line-height:1.45;font-weight:600}
.post.highlight h4{color:var(--blue)}
.view-all{position:absolute;left:548px;top:456px;display:flex;align-items:center;gap:12px;font-family:"Montserrat",Arial,sans-serif;font-size:11px;font-weight:700;letter-spacing:1px;color:var(--blue)}
.view-all .circle-btn{position:static;width:30px;height:30px}

/* FOOTER */
.site-footer{top:3080px;height:540px;background:var(--footer);overflow:hidden}
.footer-visual{position:absolute;right:0;top:0;width:640px;height:540px;background:linear-gradient(120deg,rgba(243,241,239,1) 0%,rgba(206,214,226,.7) 55%,rgba(150,170,200,.6) 100%)}
.contact-form{position:absolute;left:132px;top:60px;width:430px}
.site-footer h3{font-size:19px;font-weight:700}
.field{margin-top:14px;height:34px;border:1px solid #d2d5db;background:var(--white);font-size:11px;color:var(--muted);padding:0 12px;display:flex;align-items:center}
.contact-form .field:first-of-type{margin-top:24px}
.field.message{height:92px;align-items:flex-start;padding-top:10px}
.btn-send{margin-top:34px;width:110px;height:36px;border-radius:18px;background:var(--blue);color:var(--white);font-size:12px;font-weight:700;display:flex;align-items:center;justify-content:center}
.support{position:absolute;left:636px;top:60px;width:300px;font-size:12px;line-height:1.7}
.support .call{margin-top:16px;font-family:"Montserrat",Arial,sans-serif;font-size:16px;font-weight:700}
.support .mail{font-size:11px;color:var(--muted)}
.support .company{margin-top:16px;font-weight:600}
.support .addr{color:var(--muted);font-size:11px}
.support h4{margin-top:18px;font-size:12px;font-weight:700}
.links{display:grid;grid-template-columns:1fr 1fr;column-gap:24px;margin-top:6px;font-size:11px;color:var(--muted)}
.copy{margin-top:26px;font-size:10px;color:var(--blue);line-height:1.5}
.side-dots{position:absolute;left:1048px;top:320px;display:flex;flex-direction:column;gap:86px}
.side-dots .circle-btn{position:static;width:36px;height:36px}
</style>
</head>
<body>

<header class="hero">
  <div class="brand"><span class="mark"></span>KOVRILEX</div>
  <nav class="nav">
    <span class="active">HOME</span><span>SERVICE</span><span>BLOG</span><span>TEAM</span><span>CONTACT</span>
    <span class="phone">CALL &#9742; 800 555 010</span>
  </nav>
  <div class="btn btn-download">
    <svg width="14" height="14" viewBox="0 0 14 14"><path d="M7 1v8M3.5 5.5 7 9l3.5-3.5M2 12h10" stroke="#1f2330" stroke-width="1.8" fill="none"/></svg>
    DOWNLOAD
  </div>
  <div class="hero-art" role="img" aria-label="Isometric illustration of remote database administrators working at servers and screens"></div>
  <h1>Helping Small and medium business companies requiring remote Database Administration services!</h1>
  <div class="btn btn-consult">CONSULT NOW!</div>
  <div class="circle-btn solid" style="left:578px;top:578px;z-index:2">
    <svg width="14" height="14" viewBox="0 0 14 14"><path d="M5 3l4 4-4 4" stroke="#fff" stroke-width="2" fill="none"/></svg>
  </div>
</header>

<section class="welcome">
  <h2>Welcome to KOVRILEX<sup>.cz</sup></h2>
  <div class="sub">Remote Database Administration services</div>
  <p>Kovrilex.cz is the trusted partner for every team that runs critical data. We monitor, tune and protect your databases around the clock, so your people can focus on the business while our administrators quietly keep every system healthy, fast and secure.</p>
  <div class="circle-btn outline" style="left:636px;top:208px;width:30px;height:30px">
    <svg width="10" height="10" viewBox="0 0 14 14"><path d="M5 3l4 4-4 4" stroke="#1d9bf0" stroke-width="2" fill="none"/></svg>
  </div>
</section>

<section class="features">
  <div class="photo" role="img" aria-label="Photo of two engineers working at a server rack" style="left:112px;top:30px;width:480px;height:320px;background:linear-gradient(135deg,#5d7590,#2d3d55 60%,#1b2a40)"></div>
  <div class="feature feature-a">
    <h3>Oversee Database Administration and Management</h3>
    <p>We supervise your in-house database administrators, review their daily work, set clear standards and step in when a problem grows. You keep full control while our seniors watch every detail.</p>
    <div class="learn"><span class="dot"><svg width="10" height="10" viewBox="0 0 14 14"><path d="M5 3l4 4-4 4" stroke="#1d9bf0" stroke-width="2" fill="none"/></svg></span>LEARN MORE</div>
  </div>
  <div class="feature feature-b">
    <h3>Consult and Train the Personnel Responsible for the Database Operations</h3>
    <p>Our trainers teach your staff how to run backups, plan upgrades and solve incidents with confidence. Practical workshops and on-call advice help the people responsible for operations grow every single month.</p>
    <div class="learn"><span class="dot"><svg width="10" height="10" viewBox="0 0 14 14"><path d="M5 3l4 4-4 4" stroke="#1d9bf0" stroke-width="2" fill="none"/></svg></span>LEARN MORE</div>
  </div>
  <div class="photo" role="img" aria-label="Photo of a consultant training a team at a meeting table" style="left:608px;top:380px;width:480px;height:310px;background:linear-gradient(135deg,#dfe3e8,#aab3bf 55%,#6f7784)"></div>
</section>

<section class="services">
  <div class="service" style="left:166px">
    <svg class="icon" viewBox="0 0 70 70"><g fill="none" stroke="#1d9bf0" stroke-width="3"><ellipse cx="35" cy="16" rx="20" ry="7"/><path d="M15 16v38c0 4 9 7 20 7s20-3 20-7V16M15 29c0 4 9 7 20 7s20-3 20-7M15 42c0 4 9 7 20 7s20-3 20-7"/></g></svg>
    <h4>Remote Database</h4>
    <p>Monitoring, tuning and backup of your servers from our remote centre, with fast reaction to every alert.</p>
    <div class="circle-btn outline"><svg width="12" height="12" viewBox="0 0 14 14"><path d="M5 3l4 4-4 4" stroke="#1d9bf0" stroke-width="2" fill="none"/></svg></div>
  </div>
  <div class="service" style="left:475px">
    <svg class="icon" viewBox="0 0 70 70"><g fill="none" stroke="#1d9bf0" stroke-width="3"><rect x="10" y="10" width="40" height="46" rx="3"/><path d="M18 22h24M18 32h24M18 42h14"/><circle cx="50" cy="50" r="11" fill="#fff"/><path d="M50 43v14M43 50h14"/></g></svg>
    <h4>Database Development</h4>
    <p>Design of schemas, queries and procedures that keep your applications quick, stable and easy to extend.</p>
    <div class="circle-btn outline"><svg width="12" height="12" viewBox="0 0 14 14"><path d="M5 3l4 4-4 4" stroke="#1d9bf0" stroke-width="2" fill="none"/></svg></div>
  </div>
  <div class="service" style="left:784px">
    <svg class="icon" viewBox="0 0 70 70"><g fill="none" stroke="#1d9bf0" stroke-width="3"><rect x="12" y="8" width="46" height="14" rx="2"/><rect x="12" y="28" width="46" height="14" rx="2"/><rect x="12" y="48" width="46" height="14" rx="2"/><circle cx="20" cy="15" r="2"/><circle cx="20" cy="35" r="2"/><circle cx="20" cy="55" r="2"/></g></svg>
    <h4>Data Administration</h4>
    <p>Care for data quality, access rights and documentation, so every record stays correct and safe.</p>
    <div class="circle-btn outline"><svg width="12" height="12" viewBox="0 0 14 14"><path d="M5 3l4 4-4 4" stroke="#1d9bf0" stroke-width="2" fill="none"/></svg></div>
  </div>
</section>

<section class="team">
  <svg class="arrow" style="left:40px" width="16" height="24" viewBox="0 0 16 24"><path d="M12 4 4 12l8 8" stroke="#fff" stroke-width="2.5" fill="none"/></svg>
  <div class="member" style="left:112px">
    <div class="portrait" role="img" aria-label="Portrait photo of a team member"></div>
    <div class="name">Tomas Verner</div><div class="role">Database Architect</div>
  </div>
  <div class="member featured" style="left:360px">
    <div class="portrait" role="img" aria-label="Portrait photo of a team member"></div>
    <div class="name">Lena Marsh</div><div class="role">Consultant</div>
  </div>
  <div class="member" style="left:608px">
    <div class="portrait" role="img" aria-label="Portrait photo of a team member"></div>
    <div class="name">Oskar Hale</div><div class="role">Engineer</div>
  </div>
  <div class="member" style="left:860px">
    <div class="portrait" role="img" aria-label="Portrait photo of a team member"></div>
    <div class="name">Petr Dvorsky</div><div class="role">Business Analyst</div>
  </div>
  <svg class="arrow" style="left:1144px" width="16" height="24" viewBox="0 0 16 24"><path d="M4 4l8 8-8 8" stroke="#fff" stroke-width="2.5" fill="none"/></svg>
</section>

<section class="blog">
  <article class="blog-card">
    <div class="visual" role="img" aria-label="Photo of a caped hero action figure against a pale sky"></div>
    <div class="shade"></div>
    <div class="tag">BUSINESS INSIGHTS</div>
    <div class="date">06 JUL 2018</div>
    <h3>Everything you want to know about domains</h3>
  </article>
  <div class="blog-list">
    <div class="post highlight"><div class="date">06 JUL 2018</div><h4>Web design experts. What they can do to help you and where to find them</h4></div>
    <div class="post"><div class="date">17 JUN 2018</div><h4>Professional e-mailing guide</h4></div>
    <div class="post"><div class="date">28 MAY 2018</div><h4>PPC Advertising - How it works and what to watch out for</h4></div>
  </div>
  <div class="view-all">
    <span class="circle-btn solid"><svg width="10" height="10" viewBox="0 0 14 14"><path d="M5 3l4 4-4 4" stroke="#fff" stroke-width="2" fill="none"/></svg></span>
    VIEW ALL
  </div>
</section>

<footer class="site-footer">
  <div class="footer-visual" role="img" aria-label="Faint photo of a glass office building"></div>
  <form class="contact-form">
    <h3>Get in Touch With Us</h3>
    <div class="field">Your Name</div>
    <div class="field">Email</div>
    <div class="field">Phone</div>
    <div class="field message">Type your message</div>
    <div class="btn btn-send">SEND</div>
  </form>
  <div class="support">
    <h3>Technical info and support</h3>
    <div class="call">CALL &#9742; 800 555 010</div>
    <div class="mail">info@kovrilex.cz</div>
    <div class="company">KOVRILEX<sup>.cz</sup></div>
    <div class="addr">Lipová 12, 110 00 Praha 1, Czechia</div>
    <h4>Quick Link</h4>
    <div class="links">
      <span>About</span><span>Summary of terms</span>
      <span>Help &amp; Support</span><span>Terms and Conditions</span>
      <span>Blog</span><span>Privacy Policy</span>
      <span>Contact</span><span></span>
    </div>
    <div class="copy">© 2018 KOVRILEX.cz<br>All rights reserved</div>
  </div>
  <div class="side-dots">
    <span class="circle-btn solid"><svg width="14" height="14" viewBox="0 0 14 14"><path d="M7 1c-2.5 0-4.5 2-4.5 4.5C2.5 9 7 13 7 13s4.5-4 4.5-7.5C11.5 3 9.5 1 7 1z" fill="#fff"/></svg></span>
    <span class="circle-btn solid"><svg width="12" height="12" viewBox="0 0 14 14"><path d="M3 9l4-4 4 4" stroke="#fff" stroke-width="2" fill="none"/></svg></span>
  </div>
</footer>

</body>
</html>
```